Gardening and life coaching business card design

I need business cards for a new company in the heart of the Ozarks at the Lake of the Ozarks. Tarsey Brook Unlimited's mission is to teach the world to fish. We provide fresh local fish and produce using permaculture methods. We work with nature and the flow to create more harmony and less impact. We also coach others who are ready to make this transition. We specialize in microgreens and Aquaculture systems. I would like to make Tarsey Brook Unlimited come alive with green vines and purple flowers I wold like Tarsey Brook Unlimited to be in green and the rest of the lettering to be in purple. The feel of the card should be that of the Garden of Eden.

Life Coaching

Tarsey Brook Unlimited
Owner/Operator Delphine Hargrove
Contact Info:
(573) 204-6658
tarseybrookunlimited.com
tarseybrookunlimited is also on FB

```html
<!DOCTYPE html>
<html lang="en">
<head>
<meta charset="utf-8">
<title>Tarsey Brook Unlimited – Business Cards</title>
<link rel="stylesheet" href="https://fonts.googleapis.com/css2?family=Alegreya:wght@400;500&family=Raleway:wght@400;500&display=swap">
<style>
  :root {
    --backdrop: #e7e6e1;
    --lime: #8cc63f;
    --forest: #3f7d2b;
    --forest-deep: #2f6a22;
    --paper: #eef0e6;
    --fold: #c9ccbd;
    --serif: "Alegreya", Georgia, serif;
    --sans: "Raleway", Arial, sans-serif;
  }
  * { box-sizing: border-box; margin: 0; padding: 0; }
  html, body {
    width: 1200px; height: 1000px; overflow: hidden;
    background: var(--backdrop);
  }
  .sheet {
    position: relative; width: 1200px; height: 1000px;
    display: flex; align-items: center; justify-content: center; gap: 40px;
  }
  .card {
    position: relative; width: 530px; height: 300px;
    border-radius: 4px; overflow: hidden;
    box-shadow: 0 10px 24px rgba(0,0,0,0.18), 0 2px 4px rgba(0,0,0,0.12);
  }

  /* Brand name: one font, one weight, one colour, one size */
  .brand-name {
    font-family: var(--serif); font-weight: 400; color: var(--forest);
    white-space: nowrap; line-height: 1.2;
  }

  /* Front */
  .card--front {
    background: var(--lime);
    display: flex; align-items: center; justify-content: center;
  }
  .card--front .brand-name { font-size: 40px; }

  /* Back */
  .card--back { background: var(--paper); }
  .back__fold { position: absolute; left: 0; top: 0; }
  .back__brand {
    position: absolute; left: 12px; top: 110px; width: 196px;
    text-align: center;
  }
  .back__brand .brand-name { font-size: 18px; }
  .back__contact {
    position: absolute; left: 250px; right: 20px; top: 42px;
    text-align: center;
  }
  .contact__name {
    font-family: var(--serif); font-weight: 500; font-size: 27px;
    color: var(--forest); letter-spacing: 0.02em;
  }
  .contact__role {
    font-family: var(--sans); font-size: 18px; color: var(--forest);
    margin-top: 4px; letter-spacing: 0.02em;
  }
  .contact__phone {
    font-family: var(--sans); font-size: 20px; color: var(--forest);
    margin-top: 22px; letter-spacing: 0.04em;
  }
  .contact__social {
    display: block; width: 26px; height: 26px; border-radius: 50%;
    background: var(--forest-deep); margin: 10px auto 0;
  }
  .back__band {
    position: absolute; left: 0; right: 0; bottom: 0; height: 66px;
    background: var(--lime);
    display: flex; align-items: center; justify-content: flex-end; padding-right: 34px;
  }
  .band__web {
    font-family: var(--serif); font-size: 25px; color: var(--forest-deep);
    letter-spacing: 0.03em;
  }
</style>
</head>
<body>
<main class="sheet">
  <section class="card card--front" aria-label="Card front">
    <p class="brand-name">Tarsey Brook Unlimited</p>
  </section>

  <section class="card card--back" aria-label="Card back">
    <svg class="back__fold" width="530" height="300" viewBox="0 0 530 300" aria-hidden="true">
      <line x1="215" y1="30" x2="262" y2="205" stroke="var(--fold)" stroke-width="2"/>
    </svg>
    <div class="back__brand">
      <p class="brand-name">Tarsey Brook Unlimited</p>
    </div>
    <div class="back__contact">
      <p class="contact__name">Delphine Hargrove</p>
      <p class="contact__role">Owner/Operator</p>
      <p class="contact__phone">(573) 204-6658</p>
      <span class="contact__social" aria-label="Social page"></span>
    </div>
    <div class="back__band">
      <p class="band__web">tarseybrookunlimited.com</p>
    </div>
  </section>
</main>
</body>
</html>
```